Consulting Company Business Card

I am looking for a minimalist, classy, professional design on my business card. I would like it to be double-sided. I want to use the font and color scheme of my logo which are attached. Please be creative in the designs that you send me. I want to play off the design of my logo with the inner C that is Green and Blue broken up with the white.
Target Market(s)
Small Businesses
Industry/Entity Type
Consulting
Contact Information for Business Card
Dale M. Whitcombe, CPA CGMA, 555-014-2873, dwhitcombe@vorantaadvisory.example, www.vorantaadvisory.example

```html
<!DOCTYPE html>
<html lang="en">
<head>
<meta charset="utf-8">
<title>Voranta Advisory – Business Card</title>
<link href="https://fonts.googleapis.com/css2?family=Montserrat:wght@400;500;600;800&display=swap" rel="stylesheet">
<style>
  :root {
    --navy: #21284d;
    --teal: #0b7b7d;
    --white: #ffffff;
    --stage: #e6e7ea;
    --card-w: 520px;
    --card-h: 297px;
  }
  * { margin: 0; padding: 0; box-sizing: border-box; }
  html, body { width: 1200px; height: 801px; overflow: hidden; }
  body {
    background: var(--stage);
    font-family: "Montserrat", Arial, sans-serif;
    display: flex;
    align-items: center;
    justify-content: center;
    gap: 40px;
  }
  .card {
    position: relative;
    width: var(--card-w);
    height: var(--card-h);
    border-radius: 20px;
    overflow: hidden;
    box-shadow: 0 6px 18px rgba(0,0,0,0.18);
  }

  /* Front */
  .card--front {
    background: var(--white);
    display: flex;
    flex-direction: column;
    align-items: center;
    justify-content: center;
  }
  .brand {
    display: flex;
    align-items: center;
    gap: 14px;
    margin-top: 10px;
  }
  .brand__dot {
    width: 22px; height: 22px;
    border-radius: 50%;
    background: var(--teal);
  }
  .brand__name {
    color: var(--navy);
    font-weight: 800;
    font-size: 34px;
    letter-spacing: 1px;
    text-transform: uppercase;
    line-height: 1;
  }
  .front__web {
    margin-top: 70px;
    color: var(--navy);
    font-weight: 600;
    font-size: 12px;
    letter-spacing: 0.3px;
  }

  /* Back */
  .card--back { background: var(--navy); }
  .back__arc {
    position: absolute;
    width: 440px; height: 440px;
    border-radius: 50%;
    background: var(--white);
    left: 250px;
    top: -230px;
  }
  .holder {
    position: absolute;
    left: 38px;
    top: 138px;
  }
  .holder__name {
    color: var(--teal);
    font-weight: 500;
    font-size: 24px;
    line-height: 1.1;
  }
  .holder__title {
    margin-top: 6px;
    color: var(--white);
    font-size: 13px;
    font-weight: 400;
    letter-spacing: 0.3px;
  }
  .contacts {
    position: absolute;
    left: 230px;
    bottom: 30px;
    list-style: none;
  }
  .contacts__item {
    display: flex;
    align-items: center;
    gap: 8px;
    color: var(--white);
    font-size: 12px;
    line-height: 1;
    margin-top: 8px;
  }
  .contacts__icon { width: 13px; height: 13px; flex: none; }
</style>
</head>
<body>

  <section class="card card--front" aria-label="Card front">
    <div class="brand">
      <span class="brand__dot"></span>
      <span class="brand__name">Voranta Advisory</span>
    </div>
    <p class="front__web">www.vorantaadvisory.example</p>
  </section>

  <section class="card card--back" aria-label="Card back">
    <div class="back__arc"></div>
    <div class="holder">
      <p class="holder__name">Dale M. Whitcombe</p>
      <p class="holder__title">CPA CGMA</p>
    </div>
    <ul class="contacts">
      <li class="contacts__item">
        <svg class="contacts__icon" viewBox="0 0 24 24" aria-hidden="true"><path fill="#0b7b7d" d="M6.6 10.8a15 15 0 0 0 6.6 6.6l2.2-2.2a1 1 0 0 1 1-.25 11.4 11.4 0 0 0 3.6.57 1 1 0 0 1 1 1V20a1 1 0 0 1-1 1A17 17 0 0 1 3 4a1 1 0 0 1 1-1h3.5a1 1 0 0 1 1 1c0 1.25.2 2.45.57 3.57a1 1 0 0 1-.25 1z"/></svg>
        555-014-2873
      </li>
      <li class="contacts__item">
        <svg class="contacts__icon" viewBox="0 0 24 24" aria-hidden="true"><path fill="#0b7b7d" d="M2 5h20v14H2z"/><path fill="none" stroke="#21284d" stroke-width="2" d="M2 5l10 8 10-8"/></svg>
        dwhitcombe@vorantaadvisory.example
      </li>
      <li class="contacts__item">
        <svg class="contacts__icon" viewBox="0 0 24 24" aria-hidden="true"><circle cx="12" cy="12" r="10" fill="#0b7b7d"/><path fill="none" stroke="#21284d" stroke-width="1.6" d="M2 12h20M12 2c3 3 3 17 0 20M12 2c-3 3-3 17 0 20"/></svg>
        www.vorantaadvisory.example
      </li>
    </ul>
  </section>

</body>
</html>
```